Etiketten-Design für Duftsprays
Liebe Kreative
Es geht um ein Premium-Etikettendesign für einen Duftspray. Das Bild der Flasche werde ich Anhängen. Das sichtbare Etikett wird 7.2 x 10.8 cm gross sein. Das Etikett wird jedoch aufklappbar sein, d.h ein Teil wird auf den ersten Blick nicht sichtbar sein.
Die Mindestschriftgrösse ist Arial 7.
Das Design soll schlicht und Premium wirken. Lumidor als Name sollte von oben nach unten geschrieben werden. Dieser Name sollte man hauptsächlich sehen, wenn man es von vorne betrachtet. Wichtig ist noch, dass beim sichtbaren Teil steht „Innenseite beachten“
Sichtbarer Teil:
Lumidor (Produktname)
Inhalt: 30 ml
Gefahrenpiktogramme (Im Anhang. Auf Etikette 1x1cm gross)
Pelsa GMBH
CH-8517 Hettlingen
Tel. 022 384 57 90
Enthält / Contient: 2-Propanol
Lumidor zweimal auf Kopfhöhe und 30cm vor dem Gesicht in die Luft sprühen und einatmen. Fördert die Konzentration und macht wach.
Innenseite beachten.
Nicht sichtbarer Teil:
ACHTUNG Kann Schläfrigkeit und Benommenheit verursachen Enthält D-Limonen, Citral. Kann allergische Reaktionen hervorrufen. Darf nicht in die Hände von Kindern gelangen.
ATTENTION Peut provoquer somnolence ou vertiges. Contient d-limonène, citral. Peut produire une réaction allergique. Tenir hors de portée des enfants.
Haltbarkeit: Nach dem Öffnen 6 Monate haltbar
Aufgabenstellung
Es ist wichtig, dass das ganze Stilvoll aussieht, es soll eine 'Premium-Ausstrahlung' haben.

```html
<!DOCTYPE html>
<html lang="de">
<head>
<meta charset="utf-8">
<title>Lumidor – Etikett</title>
<link rel="stylesheet" href="https://fonts.googleapis.com/css2?family=Archivo+Black&family=Arimo:wght@400;700&display=swap">
<style>
  :root {
    --canvas-bg: #e6e7e9;
    --label-black: #04060c;
    --glow-blue: #1f46d6;
    --glow-deep: #0b1a6b;
    --name-silver: #dfe3ea;
    --info-panel-top: #eef1f7;
    --info-panel-bottom: #c9d3e8;
    --info-text: #2a2d33;
    --hazard-red: #d2161e;
  }
  * { margin: 0; padding: 0; box-sizing: border-box; }
  html, body {
    width: 983px;
    height: 1200px;
    overflow: hidden;
    background: var(--canvas-bg);
  }
  .label-sheet {
    position: absolute;
    top: 300px;
    left: 60px;
    display: flex;
    gap: 63px;
  }
  .label-panel {
    width: 400px;
    height: 600px;
    position: relative;
    overflow: hidden;
    background: var(--label-black);
    box-shadow: 0 6px 18px rgba(0,0,0,0.18);
  }
  .front-glow {
    position: absolute;
    inset: 0;
    background:
      radial-gradient(ellipse 55% 60% at 35% 45%, rgba(120,150,255,0.55) 0%, var(--glow-blue) 30%, var(--glow-deep) 60%, transparent 85%),
      linear-gradient(90deg, var(--label-black) 0%, #07113d 45%, var(--label-black) 100%);
  }
  .product-name {
    position: absolute;
    top: 50%;
    left: 50%;
    transform: translate(-50%, -50%);
    writing-mode: vertical-rl;
    font-family: "Archivo Black", sans-serif;
    font-size: 92px;
    font-weight: 400;
    letter-spacing: 6px;
    line-height: 1;
    color: var(--name-silver);
  }
  .info-panel {
    position: absolute;
    top: 36px;
    bottom: 36px;
    left: 22px;
    right: 22px;
    background: linear-gradient(180deg, var(--info-panel-top) 0%, var(--info-panel-bottom) 100%);
    padding: 30px 24px 22px;
    font-family: "Arimo", sans-serif;
    color: var(--info-text);
    font-size: 14px;
    line-height: 1.4;
  }
  .info-panel p { margin-bottom: 22px; }
  .content-volume { font-size: 15px; }
  .company-address {
    font-style: normal;
    margin-bottom: 22px;
  }
  .hazard-row {
    display: flex;
    gap: 14px;
    margin: 4px 0 18px;
  }
  .hazard-row svg { width: 56px; height: 56px; }
  .info-panel .inside-note { margin-bottom: 0; }
</style>
</head>
<body>
  <main class="label-sheet">
    <section class="label-panel label-front">
      <div class="front-glow" role="img" aria-label="Blauer Lichtschein mit Punktraster auf schwarzem Grund"></div>
      <h1 class="product-name">LUMIDOR</h1>
    </section>

    <section class="label-panel label-back">
      <div class="info-panel">
        <p class="content-volume">Inhalt: 30 ml</p>
        <p class="usage">Lumidor zweimal auf Kopfhöhe und 30cm vor dem Gesicht in die Luft sprühen und einatmen. Fördert die Konzentration und macht wach.</p>
        <address class="company-address">
          Pelsa GMBH<br>
          CH-8517 Rütiberg<br>
          Tel. 022 384 57 90
        </address>
        <p class="ingredients">Enthält / Contient: 2-Propanol</p>
        <div class="hazard-row">
          <svg viewBox="0 0 56 56" role="img" aria-label="Gefahrenpiktogramm Ausrufezeichen">
            <rect x="11" y="11" width="34" height="34" transform="rotate(45 28 28)" fill="#fff" stroke="var(--hazard-red)" stroke-width="4"/>
            <rect x="25.5" y="14" width="5" height="19" rx="1.5" fill="#111"/>
            <circle cx="28" cy="39" r="3" fill="#111"/>
          </svg>
          <svg viewBox="0 0 56 56" role="img" aria-label="Gefahrenpiktogramm Flamme">
            <rect x="11" y="11" width="34" height="34" transform="rotate(45 28 28)" fill="#fff" stroke="var(--hazard-red)" stroke-width="4"/>
            <path d="M28 14 C32 20 37 24 36 32 C35 37 32 40 28 40 C24 40 21 37 20 32 C20 27 24 25 25 20 C27 24 27 26 28 27 C29 23 29 18 28 14 Z" fill="#111"/>
            <rect x="18" y="41" width="20" height="3" fill="#111"/>
          </svg>
        </div>
        <p class="inside-note">Innenseite beachten.</p>
      </div>
    </section>
  </main>
</body>
</html>
```